Website Design for Student education travel business
GlenPath Trips
Website Design for Student education travel business - Education
Creative Brief
Education
www.glenpathtrips.example
GlenPath engages students 9-16 years of age in exciting curriculum based education travel programs. We provide students with fun hands-on and tangible educational experiences beyond the classroom that encourage a love for life-long learning. Currently, majority of our students will originate in Africa and other foreign countries with travel destinations in North America, Europe, Australia, the Caribbean and some parts of Africa. The website should convey a sense of excitement, wonder, adventure, fun, and learning for students through travel. More specifically it should also covey the sense of students exploring the amazing world around them.
Tagline for the logo is explore the amazing world around you and the website design should convey this as well as be professional for parents and teachers to confidence in our company. Stock photography should include a diverse selection of children (including children of African descent).
left side
http://www.brightmapyouthjourneys.example
http://www.learnroamvoyage.example
http://www.kplo.example
Logo has been designed for this website and will be uploaded. This site will be a static website have the ability to transition into a content management site at a latter time.

```html
<!DOCTYPE html>
<html lang="en">
<head>
<meta charset="utf-8">
<title>GlenPath Trips – Explore the amazing world around you</title>
<link rel="stylesheet" href="https://fonts.googleapis.com/css2?family=Open+Sans:wght@400;600;700;800&display=swap">
<style>
:root{
  --sky-top:#dfe7ea;
  --sky-bottom:#5a7482;
  --paper:#f8f6ef;
  --paper-line:#d9d4c4;
  --ink:#4a4a45;
  --ink-soft:#77756d;
  --green:#7cb82f;
  --green-dark:#5e9a1c;
  --blue:#2a9fd8;
  --blue-dark:#1c7fb5;
  --cream:#fffdf6;
}
*{box-sizing:border-box;margin:0;padding:0}
html,body{width:1200px;height:1000px;overflow:hidden}
body{
  font-family:"Open Sans",Arial,sans-serif;
  color:var(--ink);
  background:linear-gradient(180deg,var(--sky-top) 0%,#b9c8cf 45%,var(--sky-bottom) 100%);
  position:relative;
}
.page{
  position:absolute;left:284px;top:0;width:632px;height:1000px;
  background:var(--paper);
  box-shadow:0 0 14px rgba(40,60,70,.35);
}
.header-art{
  position:absolute;left:150px;top:0;width:482px;height:150px;
  background:linear-gradient(180deg,#cfe7f4 0%,#e9f4f9 60%,var(--paper) 100%);
}
.logo{position:absolute;left:24px;top:22px;width:160px}
.logo-name{display:flex;align-items:center;gap:8px;font-weight:800;font-size:24px;color:var(--green-dark);line-height:1}
.logo-mark{width:18px;height:18px;border-radius:50%;background:var(--blue)}
.logo-tagline{margin-top:6px;font-size:9px;font-weight:600;color:var(--ink-soft)}
.nav{position:absolute;left:34px;top:152px;display:flex;gap:10px}
.nav a{
  display:block;padding:4px 10px;border-radius:10px;background:var(--green);
  color:#fff;font-size:9px;font-weight:700;text-decoration:none;letter-spacing:.3px;
}
.nav a.current{background:var(--blue)}
.tear{position:absolute;left:14px;width:604px;height:0;border-top:2px dashed var(--paper-line)}
.main{position:absolute;left:18px;top:206px;width:388px}
.hero{
  width:300px;height:168px;margin:0 auto;border:8px solid #fff;
  box-shadow:0 2px 6px rgba(0,0,0,.25);
  background:linear-gradient(180deg,#7da79a 0%,#5f8c7e 50%,#c9b49a 100%);
}
.feature{margin-top:34px}
.feature + .feature{margin-top:20px}
.feature h2{font-size:11px;font-weight:700;color:var(--ink)}
.feature h2 span{color:var(--green)}
.feature p{margin-top:4px;font-size:7.5px;line-height:1.55;color:var(--ink-soft)}
.more{display:block;text-align:right;font-size:7.5px;font-weight:700;color:var(--green-dark);margin-top:2px}
.follow{
  position:absolute;left:18px;top:744px;width:388px;height:60px;
  background:var(--cream);border:1px solid var(--paper-line);display:flex;align-items:center;gap:10px;padding:0 12px;
}
.follow-icon{width:26px;height:26px;background:var(--blue);border-radius:4px;flex:none}
.follow p{font-size:8px;color:var(--ink-soft);line-height:1.5}
.links{position:absolute;left:18px;top:818px;width:388px}
.links h3{font-size:10px;font-weight:700;color:var(--green-dark)}
.link-cols{display:flex;justify-content:space-between;margin-top:10px}
.link-cols ul{list-style:none;font-size:7px;line-height:1.9;color:var(--ink)}
.link-cols li:first-child{font-weight:700}
.footer{position:absolute;left:0;top:972px;width:424px;text-align:center;font-size:7px;color:var(--ink-soft)}
.sidebar{position:absolute;left:424px;top:180px;width:190px}
.tab{
  display:inline-block;background:var(--blue);color:#fff;font-size:9px;font-weight:700;
  padding:4px 10px;border-radius:0 10px 10px 0;margin-left:-6px;
}
.newsletter{background:#5d7a3a;color:#fff;font-size:8px;font-weight:700;padding:5px 8px;margin-left:-6px;width:196px}
.newsletter-btn{display:block;width:60px;margin:5px auto 0;background:var(--cream);color:var(--blue-dark);text-align:center;font-size:8px;font-weight:700;padding:2px 0;border-radius:3px}
.block{margin-top:26px}
.field{height:12px;border-bottom:1px solid var(--paper-line);margin:8px 6px 0}
.search-btn{display:block;margin:8px 6px 0 auto;width:40px;text-align:center;background:var(--green);color:#fff;font-size:8px;font-weight:700;padding:2px 0;border-radius:8px}
.event-photo{
  width:158px;height:120px;margin:10px auto 0;border:6px solid #fff;
  box-shadow:0 2px 6px rgba(0,0,0,.25);
  background:linear-gradient(180deg,#b9c9d3 0%,#8d6e6e 60%,#3f4c5c 100%);
}
.post{margin-top:8px;font-size:7.5px;line-height:1.5;color:var(--ink-soft)}
.post strong{display:block;color:var(--blue-dark);font-size:8px}
.tweet{margin-top:8px;font-size:7.5px;line-height:1.5;color:var(--ink-soft);padding-bottom:6px;border-bottom:1px dashed var(--paper-line)}
</style>
</head>
<body>
<div class="page">
  <div class="header-art" role="img" aria-label="Illustrated city skyline with a rainbow and trees"></div>
  <div class="logo">
    <div class="logo-name"><span class="logo-mark"></span>GlenPath Trips</div>
    <div class="logo-tagline">Explore the amazing world around you!</div>
  </div>
  <nav class="nav">
    <a class="current" href="#">EDUCATION</a>
    <a href="#">ABOUT US</a>
    <a href="#">STUDENTS</a>
    <a href="#">PARENTS</a>
    <a href="#">TEACHERS</a>
  </nav>
  <div class="tear" style="top:182px"></div>

  <main class="main">
    <div class="hero" role="img" aria-label="Photo of a smiling group of diverse schoolchildren with backpacks in front of a chalkboard"></div>
    <section class="feature">
      <h2><span>TEACHERS</span> Inspire Your Students</h2>
      <p>Our travel programs turn lessons into living experiences. Students explore history, science and culture first hand, returning with stories, skills and a new curiosity for the world that lasts well beyond the trip.</p>
      <a class="more" href="#">LEARN MORE</a>
    </section>
    <section class="feature">
      <h2><span>STUDENTS</span> Great Adventures</h2>
      <p>Climb ancient ruins, walk through rainforests and meet young people from other lands. Every journey is packed with hands-on activities that make learning feel like the best adventure of your life.</p>
      <a class="more" href="#">LEARN MORE</a>
    </section>
    <section class="feature">
      <h2><span>PARENTS</span> Safety is Priority #1</h2>
      <p>Trained leaders travel with every group, and each itinerary is checked for safety, comfort and care. You stay informed with daily updates, so you can relax while your child discovers the world.</p>
      <a class="more" href="#">LEARN MORE</a>
    </section>
  </main>

  <div class="tear" style="top:728px;width:400px"></div>
  <div class="follow">
    <span class="follow-icon"></span>
    <p>Follow our groups live as they explore new places<br>www.glenpathtrips.example</p>
  </div>
  <div class="links">
    <h3>Important Link</h3>
    <div class="link-cols">
      <ul><li>DESTINATION</li><li>ABOUT US</li><li>STUDENTS</li><li>PARENTS</li><li>TEACHERS</li></ul>
      <ul><li>DESTINATION</li><li>ABOUT US</li><li>STUDENTS</li><li>PARENTS</li><li>TEACHERS</li></ul>
      <ul><li>DESTINATION</li><li>ABOUT US</li><li>STUDENTS</li><li>PARENTS</li><li>TEACHERS</li></ul>
      <ul><li>DESTINATION</li><li>ABOUT US</li><li>STUDENTS</li><li>PARENTS</li><li>TEACHERS</li></ul>
    </div>
  </div>
  <div class="tear" style="top:958px;width:400px"></div>
  <div class="footer">© 2013 GlenPath Trips. All rights reserved. Explore the amazing world around you.</div>

  <aside class="sidebar">
    <div class="newsletter">Newsletter Sign Up for 2013 Trips
      <span class="newsletter-btn">Get Fresh</span>
    </div>
    <div class="block">
      <span class="tab">Search Course</span>
      <div class="field"></div>
      <div class="field"></div>
      <div class="field"></div>
      <div class="field"></div>
      <span class="search-btn">search</span>
    </div>
    <div class="block">
      <span class="tab">Campus Event</span>
      <div class="event-photo" role="img" aria-label="Photo of a group of teenage students standing together outdoors"></div>
    </div>
    <div class="block">
      <span class="tab">Adventure Blog</span>
      <div class="post"><strong>2013 travel season has begun</strong>Our first groups are already landing in new places, sharing photos and stories every day.</div>
      <div class="post">Three new trips to Kenya open this spring.</div>
    </div>
    <div class="block">
      <span class="tab">Our Chirpline Feed</span>
      <div class="tweet">Our summer group reached the coast today and the views are amazing. Follow along for more updates.</div>
      <div class="tweet">Three more seats left for the Europe heritage tour, book soon.</div>
    </div>
  </aside>
</div>
</body>
</html>
```